Business card design needed

www.marlonfab.com.au
Our primary services:
On-site welding.
On-site industrial maintenance.
On-site repairs and capital works projects specialising in pipe fabrication.
Our ability to work on-site with our dedicated mobile equipment is essential to our capability to provide a quality maintenance service to our customers. We are capable of providing a full team of qualified boilermakers that can work either to your plan or project manage if a plan has not been developed.
Industry/Entity Type
Industrial
Contact Information for Business Card
company name- MARLON FAB PTY LTD
story - industrial steel fabrication, constructions and pipelines
Director - Greg Hadley
workshop address - shed 7, 3862 kemble rd Kelbrook
postal address - P.O BOX 628 KELBROOK Q 4861
mobile - 0429385106
w/shop phone - 0752937048
fax - 0752938159
email - admin@marlonfab.com.au
web - www.marlonfab.com.au
Logo Text
MARLON FAB pty ltd
Look and feel

```html
<!DOCTYPE html>
<html lang="en">
<head>
<meta charset="utf-8">
<title>Marlon Fab – Greg Hadley Business Card</title>
<link rel="stylesheet" href="https://fonts.googleapis.com/css2?family=Anton&family=Arimo&family=Libre+Baskerville&family=Tinos&display=swap">
<style>
  :root {
    --card-red: #d4100f;
    --card-red-deep: #a80808;
    --card-edge: #5a0303;
    --brand-blue: #1c1ce0;
    --name-grey: #ece6e6;
    --title-grey: #e4e0e0;
    --ink-white: #ffffff;
  }
  * { margin: 0; padding: 0; box-sizing: border-box; }
  html, body { width: 1200px; height: 695px; overflow: hidden; }
  body { background: var(--card-edge); }
  .card {
    position: relative;
    width: 1200px;
    height: 695px;
    overflow: hidden;
    color: var(--ink-white);
    font-family: "Tinos", "Times New Roman", serif;
  }
  .tread-plate {
    position: absolute;
    inset: 0;
    background: radial-gradient(ellipse at 50% 45%, var(--card-red) 0%, var(--card-red) 60%, var(--card-red-deep) 90%, var(--card-edge) 100%);
  }
  .brand {
    position: absolute;
    left: 66px;
    top: 66px;
    display: flex;
    align-items: center;
    gap: 18px;
  }
  .brand-mark {
    width: 36px;
    height: 36px;
    background: var(--brand-blue);
    flex: none;
  }
  .brand-name {
    font-family: "Arimo", Arial, sans-serif;
    font-size: 60px;
    line-height: 1.02;
    color: var(--brand-blue);
    letter-spacing: -1px;
  }
  .person {
    position: absolute;
    left: 540px;
    top: 168px;
    width: 450px;
    text-align: center;
  }
  .person-name {
    font-family: "Anton", Impact, sans-serif;
    font-weight: 400;
    font-size: 76px;
    line-height: 1;
    letter-spacing: 4px;
    color: var(--name-grey);
    text-transform: uppercase;
  }
  .person-title {
    font-family: "Libre Baskerville", Georgia, serif;
    font-size: 46px;
    line-height: 1;
    color: var(--title-grey);
    margin-top: 8px;
    letter-spacing: 1px;
    padding-left: 40px;
  }
  .phone-line {
    position: absolute;
    left: 64px;
    display: flex;
    align-items: center;
    height: 72px;
  }
  .phone-line.mobile { top: 437px; }
  .phone-line.workshop { top: 513px; }
  .phone-line.fax { top: 584px; }
  .phone-icon {
    width: 50px;
    height: 64px;
    margin-right: 22px;
    flex: none;
  }
  .phone-number {
    font-size: 57px;
    line-height: 1;
    letter-spacing: 1px;
  }
  .address-block { font-style: normal; }
  .address-line {
    position: absolute;
    left: 642px;
    top: 434px;
    font-size: 25px;
    line-height: 32px;
    letter-spacing: 0.5px;
  }
  .address-row {
    position: absolute;
    left: 640px;
    display: flex;
    align-items: center;
    height: 46px;
    font-size: 25px;
    letter-spacing: 0.8px;
  }
  .address-row.postal { top: 484px; }
  .address-row.email { top: 547px; }
  .address-icon {
    width: 76px;
    height: 46px;
    margin-right: 20px;
    flex: none;
  }
  .website {
    position: absolute;
    left: 642px;
    top: 592px;
    font-size: 45px;
    line-height: 50px;
    letter-spacing: 1px;
  }
</style>
</head>
<body>
<main class="card">
  <div class="tread-plate" role="img" aria-label="Red diamond tread plate metal texture"></div>

  <div class="brand">
    <span class="brand-mark"></span>
    <span class="brand-name">MARLON FAB<br>pty ltd</span>
  </div>

  <div class="person">
    <h1 class="person-name">Greg Hadley</h1>
    <p class="person-title">Director</p>
  </div>

  <div class="phone-line mobile">
    <svg class="phone-icon" viewBox="0 0 50 64" aria-label="Mobile">
      <rect x="6" y="2" width="38" height="60" rx="5" fill="none" stroke="#fff" stroke-width="3"/>
      <rect x="11" y="10" width="28" height="38" fill="#fff"/>
      <rect x="13" y="53" width="5" height="4" fill="#fff"/>
      <rect x="22" y="53" width="6" height="4" fill="#fff"/>
      <rect x="32" y="53" width="5" height="4" fill="#fff"/>
    </svg>
    <span class="phone-number">0429385106</span>
  </div>
  <div class="phone-line workshop">
    <svg class="phone-icon" viewBox="0 0 50 64" aria-label="Workshop phone">
      <path d="M8 6 L18 4 L22 18 L15 22 Q18 38 30 48 L36 42 L48 50 L44 60 Q28 62 16 46 Q4 30 8 6 Z" fill="none" stroke="#fff" stroke-width="3" stroke-linejoin="round"/>
    </svg>
    <span class="phone-number">0752937048</span>
  </div>
  <div class="phone-line fax">
    <svg class="phone-icon" viewBox="0 0 50 64" aria-label="Fax">
      <rect x="12" y="6" width="26" height="14" fill="#fff"/>
      <rect x="3" y="20" width="44" height="22" rx="4" fill="#fff"/>
      <rect x="12" y="36" width="26" height="22" fill="none" stroke="#fff" stroke-width="3"/>
      <line x1="17" y1="44" x2="33" y2="44" stroke="#fff" stroke-width="2"/>
      <line x1="17" y1="50" x2="33" y2="50" stroke="#fff" stroke-width="2"/>
    </svg>
    <span class="phone-number">0752938159</span>
  </div>

  <address class="address-block">
    <p class="address-line">Adress : shed 7, 3862 kemble rd Kelbrook</p>
    <div class="address-row postal">
      <svg class="address-icon" viewBox="0 0 76 46" aria-label="Postal address">
        <rect x="1.5" y="1.5" width="73" height="43" fill="none" stroke="#fff" stroke-width="2"/>
        <rect x="56" y="6" width="13" height="10" fill="#fff"/>
        <line x1="36" y1="22" x2="62" y2="22" stroke="#fff" stroke-width="2"/>
        <line x1="36" y1="28" x2="62" y2="28" stroke="#fff" stroke-width="2"/>
        <line x1="36" y1="34" x2="62" y2="34" stroke="#fff" stroke-width="2"/>
      </svg>
      <span>P.O BOX 628 KELBROOK Q 4861</span>
    </div>
    <div class="address-row email">
      <svg class="address-icon" viewBox="0 0 76 46" aria-label="Email">
        <rect x="2" y="2" width="72" height="42" fill="none" stroke="#fff" stroke-width="3"/>
        <polyline points="2,2 38,28 74,2" fill="none" stroke="#fff" stroke-width="3"/>
        <line x1="2" y1="44" x2="28" y2="22" stroke="#fff" stroke-width="3"/>
        <line x1="74" y1="44" x2="48" y2="22" stroke="#fff" stroke-width="3"/>
      </svg>
      <span>admin@marlonfab.com.au</span>
    </div>
    <p class="website">www.marlonfab.com.au</p>
  </address>
</main>
</body>
</html>
```